Frame Glow Entertainment | Business Card & Logo

We are looking for a business card with a Logo.
It’s a brand new business and we are looking for an elegant design.
The business service categories are:
Photo Booth
Photography
Events Planning
Marcus Pellham
0471926358
0381736492
info@frameglowentertainment.com.au
www.frameglowentertainment.com.au
Target Market(s)
Corporate, Photo Booth, Photography and event planning
Industry/Entity Type
Photo Booth, Photography and event planning
Contact Information for Business Card
Marcus Pellham | 0471926358 | 0381736492 | info@frameglowentertainment.com.au | www.frameglowentertainment.com.au

```html
<!DOCTYPE html>
<html lang="en">
<head>
<meta charset="utf-8">
<title>Frame Glow Entertainment – Business Card</title>
<link href="https://fonts.googleapis.com/css2?family=Lato:wght@400;700&display=swap" rel="stylesheet">
<style>
  :root {
    --backdrop: #262626;
    --card-light: #e0dfdd;
    --card-dark: #151515;
    --brown: #6f5a51;
    --gold: #c9a97a;
    --ink: #2e2b29;
  }
  * { box-sizing: border-box; margin: 0; padding: 0; }
  html, body { width: 1200px; height: 1200px; overflow: hidden; }
  body {
    background: var(--backdrop);
    font-family: "Lato", sans-serif;
    position: relative;
  }
  .card {
    position: absolute;
    left: 200px;
    width: 797px;
    height: 454px;
    border-radius: 22px;
  }
  .card--front { top: 96px; background: var(--card-light); }
  .card--back { top: 656px; background: var(--card-dark); }

  .brand {
    position: absolute;
    display: flex;
    flex-direction: column;
    align-items: center;
    color: var(--brown);
    font-weight: 400;
  }
  .brand__dot {
    border-radius: 50%;
    background: var(--gold);
  }
  .brand__name { line-height: 1.1; text-align: center; }
  .brand__rule-row { display: flex; align-items: center; }
  .brand__rule { height: 1px; background: var(--brown); }

  .card--front .brand { left: 70px; top: 140px; width: 270px; }
  .card--front .brand__dot { width: 34px; height: 34px; margin-bottom: 18px; }
  .card--front .brand__name { font-size: 36px; }
  .card--front .brand__rule-row { margin-top: 8px; gap: 10px; font-size: 15px; letter-spacing: 2px; }
  .card--front .brand__rule { width: 56px; }

  .card--back .brand { left: 0; right: 0; top: 92px; }
  .card--back .brand__dot { width: 64px; height: 64px; margin-bottom: 34px; }
  .card--back .brand__name { font-size: 64px; }
  .card--back .brand__rule-row { margin-top: 14px; gap: 14px; font-size: 24px; letter-spacing: 3px; }
  .card--back .brand__rule { width: 90px; }

  .holder {
    position: absolute;
    left: 388px;
    top: 144px;
    font-size: 33px;
    font-weight: 700;
    color: var(--brown);
    letter-spacing: 0.5px;
  }
  .holder__rule {
    position: absolute;
    left: 388px;
    right: 0;
    top: 198px;
    height: 1.5px;
    background: var(--gold);
  }
  .contacts {
    position: absolute;
    left: 394px;
    top: 218px;
    list-style: none;
    color: var(--ink);
    font-size: 18px;
  }
  .contacts li {
    display: flex;
    align-items: center;
    height: 28px;
  }
  .contacts svg { width: 14px; height: 14px; margin-right: 16px; fill: var(--brown); }
</style>
</head>
<body>
  <section class="card card--front">
    <div class="brand">
      <span class="brand__dot"></span>
      <span class="brand__name">Frame Glow</span>
      <span class="brand__rule-row"><span class="brand__rule"></span>Entertainment<span class="brand__rule"></span></span>
    </div>

    <h1 class="holder">MARCUS PELLHAM</h1>
    <div class="holder__rule"></div>

    <ul class="contacts">
      <li>
        <svg viewBox="0 0 16 16" aria-hidden="true"><path d="M3.5 1l2.5 3-1.5 1.5c.8 2 2.5 3.7 4.5 4.5L10.5 8.5l3 2.5-1.5 3C6 13.5 2.5 10 2 3.5z"/></svg>
        (047) 192-6358
      </li>
      <li>
        <svg viewBox="0 0 16 16" aria-hidden="true"><path d="M4 1h8v14H4zM5.5 2.5v9h5v-9zM7.2 12.5h1.6v1.3H7.2z" fill-rule="evenodd"/></svg>
        (038) 173-6492
      </li>
      <li>
        <svg viewBox="0 0 16 16" aria-hidden="true"><path d="M1 3h14v10H1zM2.5 4.5L8 9l5.5-4.5v7h-11z" fill-rule="evenodd"/></svg>
        info@frameglowentertainment.com.au
      </li>
      <li>
        <svg viewBox="0 0 16 16" aria-hidden="true"><path d="M8 1a7 7 0 1 0 0 14A7 7 0 0 0 8 1zm0 1.5a5.5 5.5 0 0 1 4.6 2.5H10l-1 2 2 2-1 3.5A5.5 5.5 0 0 1 3 5.5L5 7l1 3 1.5-2-1-2 2-1z" fill-rule="evenodd"/></svg>
        frameglowentertainment.com.au
      </li>
    </ul>
  </section>

  <section class="card card--back">
    <div class="brand">
      <span class="brand__dot"></span>
      <span class="brand__name">Frame Glow</span>
      <span class="brand__rule-row"><span class="brand__rule"></span>Entertainment<span class="brand__rule"></span></span>
    </div>
  </section>
</body>
</html>
```